Sales Flyer Design

Create a Flyer front and back that highlights the different things we do
We do Addition, basements, kitchens, bathrooms, concrete, siding, Roofing.

We want to highlight that we are licensed Electrical Contractor and Plumbers.
Use our Logo attached keeping color scheme mainly our company colors. We are looking for an attention grabbing but easy read for homeowners.

```html
<!DOCTYPE html>
<html lang="en">
<head>
<meta charset="utf-8">
<title>Brightline Remodeling – Flyer Front and Back</title>
<link href="https://fonts.googleapis.com/css2?family=Bebas+Neue&family=Montserrat:wght@400;500;600;700&display=swap" rel="stylesheet">
<style>
  :root {
    --stage: #636363;
    --stage-label: #7a7a7a;
    --brand-orange: #f15a29;
    --ink: #0d0d0d;
    --paper: #ffffff;
    --body-grey: #4a4a4a;
    --footer: #070707;
  }
  * { box-sizing: border-box; margin: 0; padding: 0; }
  html, body { width: 1200px; height: 835px; overflow: hidden; background: var(--stage); }
  .stage { position: relative; width: 1200px; height: 835px; }

  .side-label {
    position: absolute; top: 72px; width: 503px; text-align: center;
    font-family: "Montserrat", sans-serif; font-weight: 700; font-size: 30px;
    letter-spacing: 1px; color: var(--stage-label);
  }

  .flyer {
    position: absolute; top: 122px; width: 503px; height: 650px;
    background: var(--paper); overflow: hidden;
  }
  .flyer--front { left: 70px; }
  .flyer--back { left: 627px; }
  .side-label--front { left: 70px; }
  .side-label--back { left: 627px; }

  .flyer__band { position: absolute; left: 0; top: 0; width: 503px; height: 269px; background: var(--brand-orange); }

  .photo-frame { position: absolute; background: var(--paper); padding: 4px; }
  .photo-frame--hero { left: 43px; top: 41px; width: 417px; height: 174px; }
  .photo-frame--small { top: 218px; width: 137px; height: 102px; }
  .photo-frame--small.is-1 { left: 43px; }
  .photo-frame--small.is-2 { left: 183px; }
  .photo-frame--small.is-3 { left: 323px; }
  .photo { width: 100%; height: 100%; }

  .headline {
    position: absolute; left: 46px; top: 322px; width: 420px;
    font-family: "Bebas Neue", sans-serif; font-size: 49px; line-height: 43px;
    letter-spacing: 0.3px; white-space: nowrap;
  }
  .headline__accent { display: block; color: var(--brand-orange); }
  .headline__main { display: block; color: var(--ink); }

  .intro {
    position: absolute; left: 46px; top: 415px; width: 412px;
    font-family: "Montserrat", sans-serif; font-size: 8.6px; line-height: 11.4px;
    color: var(--body-grey); text-align: justify;
  }

  .services { position: absolute; left: 30px; top: 477px; width: 460px; display: flex; justify-content: space-between; list-style: none; }
  .service { width: 86px; display: flex; flex-direction: column; align-items: center; }
  .service__icon { width: 49px; height: 49px; border: 1px solid var(--brand-orange); display: flex; align-items: center; justify-content: center; }
  .service__icon svg { width: 32px; height: 32px; fill: none; stroke: var(--ink); stroke-width: 1.6; stroke-linejoin: round; stroke-linecap: round; }
  .service__name {
    margin-top: 6px; font-family: "Bebas Neue", sans-serif; font-size: 17px;
    color: var(--brand-orange); white-space: nowrap;
  }

  .footer { position: absolute; left: 0; top: 568px; width: 503px; height: 82px; background: var(--footer); }
  .footer__cta { position: absolute; left: 45px; top: 10px; font-family: "Bebas Neue", sans-serif; font-size: 19px; color: var(--brand-orange); }
  .footer__phone { position: absolute; left: 45px; top: 27px; font-family: "Bebas Neue", sans-serif; font-size: 34px; color: var(--paper); letter-spacing: 0.5px; }
  .footer__contact { position: absolute; left: 213px; top: 31px; font-family: "Montserrat", sans-serif; font-size: 9.4px; line-height: 13px; color: var(--paper); }
  .footer__brand { position: absolute; left: 330px; top: 24px; display: flex; align-items: center; gap: 6px; }
  .footer__brand-mark { width: 10px; height: 10px; background: var(--brand-orange); }
  .footer__brand-name { font-family: "Bebas Neue", sans-serif; font-size: 24px; line-height: 1; color: var(--paper); letter-spacing: 0.5px; }
</style>
</head>
<body>
<div class="stage">

  <div class="side-label side-label--front">FRONT</div>
  <div class="side-label side-label--back">BACK</div>

  <!-- Front side -->
  <section class="flyer flyer--front">
    <div class="flyer__band"></div>

    <div class="photo-frame photo-frame--hero">
      <div class="photo" role="img" aria-label="Remodeled bathroom with freestanding tub and glass shower" style="background:linear-gradient(135deg,#b9b7b1,#8e8b84 55%,#d8d6d0)"></div>
    </div>
    <div class="photo-frame photo-frame--small is-1">
      <div class="photo" role="img" aria-label="Aerial view of a new shingle roof" style="background:linear-gradient(135deg,#4a5040,#5d6270 50%,#3f4a3a)"></div>
    </div>
    <div class="photo-frame photo-frame--small is-2">
      <div class="photo" role="img" aria-label="Remodeled white kitchen with island" style="background:linear-gradient(180deg,#e6e4e0,#b8b3ad 60%,#4a3d3a)"></div>
    </div>
    <div class="photo-frame photo-frame--small is-3">
      <div class="photo" role="img" aria-label="Finished basement with staircase" style="background:linear-gradient(180deg,#ddd3c0,#cbbfa9 60%,#d7d2c8)"></div>
    </div>

    <h1 class="headline">
      <span class="headline__accent">Premier Local Remodeling</span>
      <span class="headline__main">Company in Ankeny, IA</span>
    </h1>

    <p class="intro">We specialize in basements, kitchens, bathrooms, concrete, siding, Roofing. remodeling. You can count on us to work directly with you throughout your entire project to make sure we bring your vision to life. We'll help you choose designs, materials and styles to completely transform the look and feel of your home.</p>

    <ul class="services">
      <li class="service">
        <div class="service__icon"><svg viewBox="0 0 32 32"><path d="M6 30V14a10 10 0 0 1 20 0v16z"/><path d="M12 30v-4h4v-4h4v-4h4"/><circle cx="16" cy="9" r="2"/></svg></div>
        <span class="service__name">Basements</span>
      </li>
      <li class="service">
        <div class="service__icon"><svg viewBox="0 0 32 32"><rect x="2" y="16" width="18" height="12"/><path d="M2 21h18M11 16v12"/><rect x="22" y="8" width="8" height="20"/><path d="M22 16h8M6 12h8l-1-4H7z"/></svg></div>
        <span class="service__name">Kitchens</span>
      </li>
      <li class="service">
        <div class="service__icon"><svg viewBox="0 0 32 32"><path d="M4 6v14h14a6 6 0 0 1-6 6H8v4h10"/><path d="M4 6h5v14"/><rect x="20" y="4" width="10" height="8"/><path d="M20 14h10l-2 5h-6zM25 19v7"/></svg></div>
        <span class="service__name">Bathrooms</span>
      </li>
      <li class="service">
        <div class="service__icon"><svg viewBox="0 0 32 32"><path d="M4 4l14 10-3 3L3 6z"/><path d="M16 16l4 6"/><path d="M2 24h28v5H2z"/><path d="M8 24v5M14 24v5M20 24v5M26 24v5"/></svg></div>
        <span class="service__name">Concrete</span>
      </li>
      <li class="service">
        <div class="service__icon"><svg viewBox="0 0 32 32"><path d="M2 26L14 6h6l10 20z"/><path d="M20 6l-10 20M8 16h18M5 21h23M14 11h10"/><path d="M22 4h3v5"/></svg></div>
        <span class="service__name">Roofing</span>
      </li>
    </ul>

    <footer class="footer">
      <div class="footer__cta">Call Now Today!</div>
      <div class="footer__phone">555-014-2280</div>
      <div class="footer__contact">www.brightlinehome.com<br>info@brightlinehome.com</div>
      <div class="footer__brand"><span class="footer__brand-mark"></span><span class="footer__brand-name">Brightline<br>Remodeling</span></div>
    </footer>
  </section>

  <!-- Back side -->
  <section class="flyer flyer--back">
    <div class="flyer__band"></div>

    <div class="photo-frame photo-frame--hero">
      <div class="photo" role="img" aria-label="Plumber's hand installing a chrome faucet" style="background:linear-gradient(135deg,#f2f2f2,#d9dde3 50%,#9fb0c8)"></div>
    </div>
    <div class="photo-frame photo-frame--small is-1">
      <div class="photo" role="img" aria-label="Electrician with cables and tools" style="background:linear-gradient(135deg,#e8e8e8,#3c4d8a 55%,#6a8a4a)"></div>
    </div>
    <div class="photo-frame photo-frame--small is-2">
      <div class="photo" role="img" aria-label="Plumber working under a sink with fittings" style="background:linear-gradient(180deg,#eceff2,#3e4f8c 45%,#e4e4e4)"></div>
    </div>
    <div class="photo-frame photo-frame--small is-3">
      <div class="photo" role="img" aria-label="Electrician testing a breaker panel" style="background:linear-gradient(135deg,#c99a5a,#e7e3da 50%,#3a4a6a)"></div>
    </div>

    <h1 class="headline">
      <span class="headline__accent">Professional Electrical</span>
      <span class="headline__main">Contractor and Plumbers</span>
    </h1>

    <p class="intro">Lorem ipsum dolor sit amet, consectetuer adipiscing elit, sed diam nonummy nibh euismod tincidunt ut laoreet dolore magna aliquam erat volutpat. Ut wisi enim ad minim veniam, quis nostrud exerci tation ullamcorper suscipit lobortis nisl ut aliquip ex ea commodo consequat. Ilum dolore eu feugiat nulla facilisis at vero eros et</p>

    <ul class="services">
      <li class="service">
        <div class="service__icon"><svg viewBox="0 0 32 32"><path d="M4 6l4-3 4 4-1 3 14 14 3-1 2 4-4 4-3-3 1-3L10 11l-3 1z"/><path d="M24 4l4 4-16 16-4 4-4-4 4-4z"/></svg></div>
        <span class="service__name">Installation</span>
      </li>
      <li class="service">
        <div class="service__icon"><svg viewBox="0 0 32 32"><path d="M2 5h28M8 5v8M16 5v8M24 5v8"/><path d="M5 19l3-6 3 6zM13 19l3-6 3 6zM21 19l3-6 3 6z"/><path d="M6 23l-1 2M10 23l1 2M14 23l-1 2M18 23l1 2M22 23l-1 2M26 23l1 2"/></svg></div>
        <span class="service__name">Lighting</span>
      </li>
      <li class="service">
        <div class="service__icon"><svg viewBox="0 0 32 32"><circle cx="16" cy="13" r="11"/><circle cx="16" cy="13" r="2"/><path d="M16 11V4M18 13h7M16 15v7M14 13H7"/><path d="M16 24v4M10 30h12"/></svg></div>
        <span class="service__name">Celling Fans</span>
      </li>
      <li class="service">
        <div class="service__icon"><svg viewBox="0 0 32 32"><ellipse cx="16" cy="6" rx="12" ry="3"/><path d="M4 6v20c0 2 5 3 12 3s12-1 12-3V6"/><path d="M4 11c0 2 5 3 12 3s12-1 12-3M4 16c0 2 5 3 12 3s12-1 12-3M4 21c0 2 5 3 12 3s12-1 12-3"/></svg></div>
        <span class="service__name">Wiring</span>
      </li>
      <li class="service">
        <div class="service__icon"><svg viewBox="0 0 32 32"><rect x="6" y="2" width="20" height="28" rx="2"/><rect x="11" y="8" width="10" height="16"/><path d="M11 16l10-4"/><circle cx="16" cy="20" r="1"/></svg></div>
        <span class="service__name">Switches</span>
      </li>
    </ul>

    <footer class="footer">
      <div class="footer__cta">Call Now Today!</div>
      <div class="footer__phone">555-014-2280</div>
      <div class="footer__contact">www.brightlinehome.com<br>info@brightlinehome.com</div>
      <div class="footer__brand"><span class="footer__brand-mark"></span><span class="footer__brand-name">Brightline<br>Remodeling</span></div>
    </footer>
  </section>

</div>
</body>
</html>
```